Meadowlark Learning Growth Partners (MLGP)

This is a professional business card. Logo and picture are a must on the front of the card. I am an educational consultant. I have been consulting for the past three years for a company. I am now opening my own company. My goal for my consulting company is to eventually consult all over America.

Target Market(s)

Educators, schools, professionals

Industry/Entity Type

Consulting

Contact Information for Business Card

Picture/logo on front, simple modern design

Font styles to use
Serif

Colors
85abd2
0355a3
3176b5
cedeed

Requirements
Must have
• picture, logo,
• Odessa Pruitt, Ed.S
• address 5073 Cormorant ridge Dr. Nashville, TN 37940
• Cell:616-555-0148
• Office: 629-555-0172
• www.Mlgpedu.example
• pruittodessa@mailbox.example

```html
<!DOCTYPE html>
<html lang="en">
<head>
<meta charset="utf-8">
<title>Meadowlark Learning Growth Partners – Business Card</title>
<link rel="stylesheet" href="https://fonts.googleapis.com/css2?family=Comfortaa:wght@700&family=Oswald:wght@500&family=Open+Sans:wght@400&display=swap">
<style>
  :root {
    --navy: #033a78;
    --brand-blue: #0355a3;
    --ink: #2b2b2b;
    --text: #1f1f1f;
    --white: #ffffff;
    --backdrop: #ecedf0;
  }
  * { margin: 0; padding: 0; box-sizing: border-box; }
  html, body { width: 1200px; height: 1000px; overflow: hidden; }
  body { background: var(--backdrop); position: relative; font-family: "Open Sans", sans-serif; }

  .card {
    position: absolute;
    left: 266px;
    width: 666px;
    height: 396px;
    box-shadow: 0 4px 14px rgba(0,0,0,0.18);
  }

  /* Front */
  .card-front { top: 74px; background: var(--navy); color: var(--white); }
  .brand-mark {
    position: absolute; left: 92px; top: 166px;
    width: 44px; height: 44px; border-radius: 50%;
    background: var(--white);
  }
  .brand-name {
    position: absolute; left: 150px; top: 166px;
    font-family: "Comfortaa", sans-serif; font-weight: 700;
    font-size: 40px; line-height: 44px; letter-spacing: 2px;
    color: var(--white);
  }
  .brand-divider {
    position: absolute; left: 358px; top: 140px;
    width: 1.5px; height: 115px; background: rgba(255,255,255,0.85);
  }
  .brand-full {
    position: absolute; left: 377px; top: 140px;
    font-family: "Comfortaa", sans-serif; font-weight: 700;
    font-size: 22px; line-height: 31px; color: var(--white);
  }

  /* Back */
  .card-back { top: 534px; background: var(--white); }
  .name-tab {
    position: absolute; left: 0; top: 94px;
    width: 16px; height: 50px; background: var(--navy);
  }
  .holder-name {
    position: absolute; left: 34px; top: 90px;
    font-family: "Oswald", sans-serif; font-weight: 500;
    font-size: 28px; line-height: 36px; letter-spacing: 0.5px;
    text-transform: uppercase; color: var(--ink);
  }
  .holder-role {
    position: absolute; left: 34px; top: 124px;
    font-size: 17px; color: var(--brand-blue);
  }
  .address {
    position: absolute; left: 33px; top: 196px;
    font-size: 16px; line-height: 24px; color: var(--text);
  }
  .contact-list {
    position: absolute; left: 32px; top: 258px;
    list-style: none; font-size: 16px; line-height: 23px; color: var(--text);
  }
  .contact-list li { display: flex; align-items: center; gap: 7px; }
  .contact-list svg { width: 14px; height: 14px; fill: var(--navy); flex: none; }
  .portrait {
    position: absolute; right: 18px; bottom: 0;
    width: 350px; height: 370px;
    background: linear-gradient(180deg, #e6d3a8 0%, #e9c9b5 40%, #f2f2f2 62%, #1e2433 78%, #151a26 100%);
    border-radius: 150px 150px 0 0;
  }
</style>
</head>
<body>

<section class="card card-front" aria-label="Card front">
  <div class="brand-mark"></div>
  <div class="brand-name">MLGP</div>
  <div class="brand-divider"></div>
  <div class="brand-full">Meadowlark<br>Learning<br>Growth<br>Partners</div>
</section>

<section class="card card-back" aria-label="Card back">
  <div class="name-tab"></div>
  <h1 class="holder-name">Odessa Pruitt, Ed.S</h1>
  <p class="holder-role">Founder / CEO</p>
  <p class="address">5073 Cormorant ridge Dr.<br>Nashville, TN 37940</p>
  <ul class="contact-list">
    <li><svg viewBox="0 0 16 16"><path d="M1 6c0-2 3-4 7-4s7 2 7 4v1h-3V5.5c-1-.5-2.5-.8-4-.8s-3 .3-4 .8V7H1zM4 8h8l2 6H2z"/></svg>629-555-0172</li>
    <li><svg viewBox="0 0 16 16"><path d="M4 1h8v14H4zM5.5 2.5v10h5v-10z"/></svg>616-555-0148</li>
    <li><svg viewBox="0 0 16 16"><path d="M1 3h14v10H1zM2 4l6 5 6-5v-.2H2z"/></svg>pruittodessa@mailbox.example</li>
    <li><svg viewBox="0 0 16 16"><path d="M8 1a7 7 0 1 0 0 14A7 7 0 0 0 8 1zm0 2a5 5 0 0 1 4.6 3H10L8 4 6 6l2 2-2 3 1 2a5 5 0 0 1 1-10z"/></svg>www.Mlgpedu.example</li>
  </ul>
  <div class="portrait" role="img" aria-label="Portrait photograph of Odessa Pruitt"></div>
</section>

</body>
</html>
```